menu boards

we would like change our prices on our boards

oatmeal prices
small $3.00
Large $4.00

lunch specials
$8.95

breakfast specials
#1 $5.00
#2 $5.00
#3 $5.00
#4 $4.00
#5 $5.95
#6 $5.25
Please order by Number - No substitutions

```html
<!DOCTYPE html>
<html lang="en">
<head>
<meta charset="utf-8">
<title>Lunch Specials</title>
<link rel="stylesheet" href="https://fonts.googleapis.com/css2?family=Alfa+Slab+One&family=Oswald:wght@700&family=Open+Sans:wght@700&display=swap">
<style>
  :root {
    --red: #e31e2d;
    --red-deep: #b5121f;
    --gold-top: #fff37a;
    --gold-bottom: #f2b705;
    --gold-line: #d88a00;
    --white: #ffffff;
    --cream: #f3ead8;
    --ink: #111111;
    --salad: #5d7a3e;
    --bread: #d9a35f;
    --soup-cup: #f3c62f;
  }
  html, body {
    margin: 0;
    padding: 0;
    width: 1200px;
    height: 943px;
    overflow: hidden;
    background: var(--white);
  }
  .board {
    position: relative;
    width: 1200px;
    height: 943px;
    background: var(--white);
  }
  .header {
    position: absolute;
    left: 0; top: 0;
    width: 1200px;
    height: 345px;
    background: var(--red);
    overflow: hidden;
  }
  .title-lunch, .title-specials {
    position: absolute;
    left: 0;
    width: 100%;
    margin: 0;
    text-align: center;
    font-family: "Alfa Slab One", serif;
    font-weight: 400;
    line-height: 1;
    -webkit-background-clip: text;
    background-clip: text;
    color: transparent;
  }
  .title-lunch {
    top: 36px;
    font-size: 118px;
    letter-spacing: 6px;
    background-image: linear-gradient(var(--gold-top), var(--gold-bottom));
    -webkit-text-stroke: 1.5px var(--gold-line);
  }
  .title-specials {
    top: 166px;
    font-size: 172px;
    letter-spacing: 6px;
    background-image: linear-gradient(var(--white) 40%, var(--cream));
    -webkit-text-stroke: 1.5px #f0c040;
  }
  .divider {
    position: absolute;
    left: 593px; top: 345px;
    width: 10px;
    height: 598px;
    background: var(--red);
  }
  .combo {
    position: absolute;
    top: 345px;
    width: 593px;
    height: 598px;
  }
  .combo--salad { left: 0; }
  .combo--soup { left: 603px; }
  .combo-label {
    position: absolute;
    top: 95px;
    height: 405px;
    writing-mode: vertical-rl;
    transform: rotate(180deg);
    font-family: "Oswald", sans-serif;
    font-weight: 700;
    font-size: 86px;
    line-height: 1;
    letter-spacing: 4px;
    color: var(--red);
    text-align: center;
  }
  .combo--salad .combo-label { left: 40px; }
  .combo--soup .combo-label { left: 42px; }
  .combo-photo {
    position: absolute;
    top: 42px;
    left: 228px;
    width: 330px;
    height: 240px;
    border-radius: 40px;
  }
  .combo--salad .combo-photo {
    background: radial-gradient(circle at 30% 30%, var(--salad) 0 30%, transparent 45%),
                linear-gradient(160deg, #e9c489, var(--bread) 60%, #c4794a);
  }
  .combo--soup .combo-photo {
    background: radial-gradient(circle at 22% 35%, var(--soup-cup) 0 25%, transparent 40%),
                linear-gradient(160deg, #e9c489, var(--bread) 60%, #c4794a);
  }
  .combo-desc {
    position: absolute;
    left: 190px;
    top: 302px;
    width: 400px;
    margin: 0;
    text-align: center;
    font-family: "Open Sans", sans-serif;
    font-weight: 700;
    font-size: 29px;
    line-height: 43px;
    color: var(--ink);
  }
  .combo--soup .combo-desc { left: 186px; }
  .combo-price {
    position: absolute;
    left: 190px;
    top: 462px;
    width: 400px;
    margin: 0;
    text-align: center;
    font-family: "Alfa Slab One", serif;
    font-size: 62px;
    line-height: 1;
    letter-spacing: 2px;
    color: var(--red);
    text-shadow: 2px 3px 0 var(--red-deep), 3px 5px 4px rgba(0,0,0,0.25);
  }
  .combo--soup .combo-price { left: 186px; }
</style>
</head>
<body>
<main class="board">
  <header class="header">
    <h1 class="title-lunch">LUNCH</h1>
    <h1 class="title-specials">SPECIALS</h1>
  </header>

  <section class="combo combo--salad">
    <div class="combo-label">COMBO #2</div>
    <div class="combo-photo" role="img" aria-label="House salad in a clear container beside a half sandwich"></div>
    <p class="combo-desc">Any Premade<br>HALF Sandwich/Wrap<br>with House Salad</p>
    <p class="combo-price">$8.95</p>
  </section>

  <div class="divider"></div>

  <section class="combo combo--soup">
    <div class="combo-label">COMBO #2</div>
    <div class="combo-photo" role="img" aria-label="Small cup of vegetable soup beside a half sandwich"></div>
    <p class="combo-desc">Any Premade<br>HALF Sandwich/Wrap<br>with sm. Soup</p>
    <p class="combo-price">$8.95</p>
  </section>
</main>
</body>
</html>
```